Colorful Live Music Concert Poster for Tin Harbor

Looking for a portrait oriented "poster" promoting the band's upcoming show at Marlow Lounge on Sunday, 3/22 at 8 pm, and social version (square format for Instagram). <br/><br/>Copy:<br/>Tin Harbor<br/>with The Pale Wires<br/><br/>Marlow Lounge <br/>Sunday, March 22<br/>8 pm<br/><br/>Poster must be consistent with band's overall branding seen on www.tinharborband.example and it's Tunevault page at https://music.example.com/artist/7QxRtaWpLeNmVcz2Ks9DuB?si=381fkTsYpWmaGHeLoRqdXC <br/><br/>BUT, we wouldn't mind taking in a slightly updated direction. A good example is the cover for our recent single Glad Today, which is consistent in theme and color palette while updating the design and color at the same time. <br/><br/>The attached files include some band logo art as well as examples of posters done for prior shows. <br/><br/>The posters need not include photos of the band, but if you are so inclined, we've uploaded some selects as well.<br/><br/>Thank you. <br/><br/>Wendell<br/>Tin Harbor

```html
<!DOCTYPE html>
<html lang="en">
<head>
<meta charset="utf-8">
<title>Tin Harbor with The Pale Wires – Marlow Lounge</title>
<link rel="stylesheet" href="https://fonts.googleapis.com/css2?family=League+Spartan:wght@200;700;800&family=Montserrat:wght@500&display=swap">
<style>
  :root {
    --teal: #6cc5c9;
    --navy: #1b2a5a;
    --white: #ffffff;
    --orange: #f7a91b;
    --tone-grey: #8d8a85;
    --tone-warm: #c98a4c;
    --tone-sky: #efeeec;
    --tone-wall: #d9d8d6;
    --tone-stripe: #e3e4ea;
    --tone-denim: #a6bccf;
    --tone-skin: #e3bca2;
  }
  * { margin: 0; padding: 0; box-sizing: border-box; }
  html, body { width: 1200px; height: 1200px; overflow: hidden; }
  body { background: var(--teal); }
  .poster {
    position: relative;
    width: 1200px;
    height: 1200px;
    background: var(--teal);
    overflow: hidden;
    font-family: "League Spartan", sans-serif;
  }
  .band-photo {
    position: absolute;
    inset: 0;
    width: 1200px;
    height: 1200px;
  }
  .dot-grid { position: absolute; }
  .dot-grid--top { left: 34px; top: 194px; }
  .dot-grid--bottom { left: 833px; top: 994px; }

  .headliner {
    position: absolute;
    font-family: "Montserrat", sans-serif;
    font-weight: 500;
    color: var(--navy);
    transform-origin: left top;
    transform: rotate(-90deg);
    white-space: nowrap;
    line-height: 1;
    font-size: 92px;
  }
  .headliner--first { left: 26px; top: 772px; letter-spacing: 14px; }
  .headliner--second { left: 116px; top: 810px; letter-spacing: 6px; }

  .support { position: absolute; left: 206px; color: var(--white); line-height: 1; white-space: nowrap; }
  .support__with { top: 420px; font-size: 84px; font-weight: 200; }
  .support__line { font-size: 116px; font-weight: 700; letter-spacing: -2px; }
  .support__line--one { top: 493px; }
  .support__line--two { top: 607px; }
  .support__line--three {
    top: 722px;
    font-weight: 200;
    color: transparent;
    -webkit-text-stroke: 2px var(--white);
    font-size: 120px;
  }

  .date-bar {
    position: absolute;
    left: 34px;
    top: 892px;
    width: 844px;
    height: 70px;
    background: var(--navy);
    color: var(--white);
    font-weight: 800;
    font-size: 45px;
    line-height: 70px;
    padding-left: 86px;
    padding-top: 4px;
    white-space: pre;
    letter-spacing: 0.5px;
  }
  .venue {
    position: absolute;
    left: 121px;
    top: 994px;
    color: var(--white);
    font-weight: 700;
    font-size: 80px;
    line-height: 1;
    white-space: nowrap;
    letter-spacing: -1px;
  }
</style>
</head>
<body>
<main class="poster">
  <svg class="band-photo" viewBox="0 0 1200 1200" role="img" aria-label="Photo of the two band members: a man playing an acoustic guitar and a smiling woman seated beside him outdoors">
    <defs>
      <clipPath id="photoArea">
        <polygon points="19,0 1200,0 1200,1196"/>
      </clipPath>
      <linearGradient id="baseTone" x1="0" y1="0" x2="1" y2="1">
        <stop offset="0" stop-color="var(--tone-grey)"/>
        <stop offset="0.5" stop-color="var(--tone-wall)"/>
        <stop offset="1" stop-color="var(--tone-stripe)"/>
      </linearGradient>
      <radialGradient id="toneSky"><stop offset="0" stop-color="var(--tone-sky)"/><stop offset="1" stop-color="var(--tone-sky)" stop-opacity="0"/></radialGradient>
      <radialGradient id="toneGrey"><stop offset="0" stop-color="var(--tone-grey)"/><stop offset="1" stop-color="var(--tone-grey)" stop-opacity="0"/></radialGradient>
      <radialGradient id="toneWarm"><stop offset="0" stop-color="var(--tone-warm)"/><stop offset="1" stop-color="var(--tone-warm)" stop-opacity="0"/></radialGradient>
      <radialGradient id="toneSkin"><stop offset="0" stop-color="var(--tone-skin)"/><stop offset="1" stop-color="var(--tone-skin)" stop-opacity="0"/></radialGradient>
      <radialGradient id="toneStripe"><stop offset="0" stop-color="var(--tone-stripe)"/><stop offset="1" stop-color="var(--tone-stripe)" stop-opacity="0"/></radialGradient>
      <radialGradient id="toneDenim"><stop offset="0" stop-color="var(--tone-denim)"/><stop offset="1" stop-color="var(--tone-denim)" stop-opacity="0"/></radialGradient>
    </defs>
    <g clip-path="url(#photoArea)">
      <rect width="1200" height="1200" fill="url(#baseTone)"/>
      <ellipse cx="1000" cy="120" rx="320" ry="220" fill="url(#toneSky)"/>
      <ellipse cx="560" cy="300" rx="320" ry="300" fill="url(#toneGrey)"/>
      <ellipse cx="260" cy="170" rx="260" ry="170" fill="url(#toneWarm)"/>
      <ellipse cx="1120" cy="330" rx="160" ry="230" fill="url(#toneSkin)"/>
      <ellipse cx="1000" cy="640" rx="260" ry="240" fill="url(#toneStripe)"/>
      <ellipse cx="1000" cy="880" rx="220" ry="200" fill="url(#toneSkin)" opacity="0.8"/>
      <ellipse cx="1160" cy="940" rx="140" ry="200" fill="url(#toneDenim)"/>
    </g>
  </svg>

  <svg class="dot-grid dot-grid--top" width="88" height="182" viewBox="0 0 88 182" aria-hidden="true">
    <pattern id="dotsTop" width="19" height="19.2" patternUnits="userSpaceOnUse">
      <circle cx="3.5" cy="3.5" r="3.2" fill="#fff"/>
    </pattern>
    <rect width="88" height="182" fill="url(#dotsTop)"/>
  </svg>

  <svg class="dot-grid dot-grid--bottom" width="120" height="182" viewBox="0 0 120 182" aria-hidden="true">
    <circle cx="36" cy="117" r="31" fill="var(--orange)"/>
    <pattern id="dotsBottom" x="35" width="19" height="19.2" patternUnits="userSpaceOnUse">
      <circle cx="3.5" cy="3.5" r="3.2" fill="#fff"/>
    </pattern>
    <rect x="35" width="85" height="182" fill="url(#dotsBottom)"/>
  </svg>

  <h1>
    <span class="headliner headliner--first">TIN</span>
    <span class="headliner headliner--second">HARBOR</span>
  </h1>

  <div class="support support__with">with</div>
  <div class="support support__line support__line--one">The</div>
  <div class="support support__line support__line--two">Pale</div>
  <div class="support support__line support__line--three">Wires</div>

  <div class="date-bar">SUNDAY, MARCH 22  8 PM</div>
  <div class="venue">At Marlow Lounge</div>
</main>
</body>
</html>
```